Corporate Identity Design Project

Teslin Varrow Design is a small boutique event planning and floral design company, based in Northern Alberta. I require the creation of some corporate identity pieces. I want a minimalistic design.
Website www.teslinvarrow.example

Pieces should include
1. Business Card
Should include the company logo, name, email address, address, phone number. These will be professional printed.
These are three cards that I like:
http://cardsamplegallery.example/wp-content/uploads/2010/02/Odile_Vantreck_Roomworks_by_Pepperleaf_studio_Media.jpg
http://neatcardshowcase.example/wp-content/uploads/2011/06/Quiet-Studio-Minimalist-Business-Cards_11.jpg
http://graphicfeedhub.example/wp-content/uploads/2012/03/16.minimalist-business-cards.jpg
I like letterpress, but I am open to other options.

2. Letterhead
will be professionally printed

3. Envelope

4. Fax Sheet
will be printed on home printer

5. Pocket Presentation
Like -http://wrenfieldgardens.example/img/design_step_proposal@2x.jpg

6. Invoice
Like - http://samplehost.example/quillmarsh/2011/02/falcon-athletics-4-letterhead-combined.png?w=529

7. Proposal
Like something like this – this will not be printed, but rather emailed to clients
Like http://files7.imagedepot.example/getfile/files.imagedepot.example/trelvo-studio/nkuBfi2LVj7ENiUb5D16wqAHQHqNNT5vut7mukSTmisfoGHYXGEv9haEQOPL/Picture-52.png.scaled.500.jpg

8. Contract
Like http://www.brightkeyadvertising.example/images/sample-contract.jpg

9. Business Brochure – I have removed this piece from the project and will most likely post it as another project at a later date.

If you think that this is a project of interest to you, but feel that it is “too much” work for the price, please let me know how you would re-package it – I am open to suggestions.

Target Market(s)

Young women

Industry/Entity Type

Boutique

Requirements
Should not have
• I do not want it to look "frilly"

```html
<!DOCTYPE html>
<html lang="en">
<head>
<meta charset="utf-8">
<title>Teslin Varrow Design — Letterhead</title>
<link rel="stylesheet" href="https://fonts.googleapis.com/css2?family=Open+Sans:wght@400;600&display=swap">
<style>
  :root {
    --backdrop: #d9d9d9;
    --paper: #ffffff;
    --ink: #4a3a35;
    --brand-brown: #6f5851;
    --brand-mauve: #8c4f50;
    --on-band: #f4eeec;
  }
  * { box-sizing: border-box; margin: 0; padding: 0; }
  html, body {
    width: 1200px; height: 877px; overflow: hidden;
    background: var(--backdrop);
    font-family: "Open Sans", Arial, sans-serif;
    color: var(--ink);
  }
  .letterhead {
    position: absolute; left: 300px; top: 50px;
    width: 600px; height: 776px;
    background: var(--paper);
    box-shadow: 0 2px 8px rgba(0,0,0,0.12);
  }
  .wordmark {
    position: absolute; display: flex; align-items: center; gap: 8px;
    font-weight: 600; letter-spacing: 0.12em; text-transform: uppercase;
  }
  .wordmark .dot { border-radius: 50%; flex: none; }
  .header-mark { left: 36px; top: 44px; font-size: 12px; color: var(--brand-brown); }
  .header-mark .dot { width: 20px; height: 20px; background: var(--brand-mauve); }
  .header-contact {
    position: absolute; left: 240px; right: 36px; top: 40px;
    display: flex; justify-content: space-between;
    font-size: 9px; font-weight: 600; padding-bottom: 4px;
    border-bottom: 1.5px solid var(--brand-brown);
  }
  .footer-contact {
    position: absolute; left: 36px; top: 696px;
    font-size: 10px; font-weight: 600; line-height: 1.4;
  }
  .footer-band {
    position: absolute; left: 230px; right: 0; top: 688px; height: 44px;
    background: var(--brand-brown); border-radius: 3px 0 0 3px;
    display: flex; align-items: center; justify-content: space-between;
    padding: 0 24px 0 14px; color: var(--on-band);
  }
  .footer-band .wordmark { position: static; font-size: 10px; color: var(--on-band); }
  .footer-band .dot { width: 18px; height: 18px; border: 1.5px solid var(--on-band); }
  .footer-address { font-size: 8.5px; font-weight: 600; line-height: 1.35; font-style: normal; }
</style>
</head>
<body>
  <main class="letterhead">
    <div class="wordmark header-mark"><span class="dot"></span>Teslin Varrow Design</div>
    <div class="header-contact">
      <span>hello@teslinvarrow.example</span>
      <span>(780) 555-0142</span>
    </div>

    <div class="footer-contact">
      <div>www.teslinvarrow.example</div>
      <div>(780) 555-0142</div>
    </div>
    <div class="footer-band">
      <div class="wordmark"><span class="dot"></span>Teslin Varrow Design</div>
      <address class="footer-address">
        Teslin Varrow Design Ltd<br>
        4410 - 52 Avenue NW<br>
        Larchmere, Alberta T0H 1K2
      </address>
    </div>
  </main>
</body>
</html>
```